Product and Services Brochure for an Oil and Gas Business

Need a brochure design for our Products and Services. I've attached expectations, Product Names, Picture link, Logo. Please ask if you have any questions.

Use Black and/or White background and related bright colors per our logo colors. Design will have black silk laminate and SPOT UV. Hence please define the respective layers and incorporate those feature in the design. Be bold, modern and unique. No cluttered designs.

Pictures link https://files.pelvanto.net/share/folders/7KqR2mTzpLw9xBnc4YdEuA0sVh-Jf3Gk?mode=view

Logos - There are two logos that we use. One for square spaces and one for horizontal spaces

Target Market(s)

Industrial

Colors

Designer to choose colors to be used in the design.

Requirements
Must have
• Clean, uncluttered and bold design with good color pairing
Nice to have
• Pictures provided have both black and transparent backgrounds. It will be great (not sure how) but keep the background dynamic so no product pic gets lost or have weird lines
Should not have
• Too much color

```html
<!DOCTYPE html>
<html lang="en">
<head>
<meta charset="utf-8">
<title>Products and Services Brochure Spread</title>
<link href="https://fonts.googleapis.com/css2?family=Montserrat:ital,wght@0,400;0,500;0,600;0,700;1,500&display=swap" rel="stylesheet">
<style>
  :root{
    --backdrop:#cfcfcf;
    --paper:#f4f4f4;
    --blue:#1d5f9e;
    --green:#5fb336;
    --green-dark:#3f9a2c;
    --green-light:#8ccf4d;
    --text:#5a5a5a;
    --white:#ffffff;
    --ring-track:#e3e3e3;
  }
  *{box-sizing:border-box;margin:0;padding:0}
  html,body{width:1200px;height:833px;overflow:hidden}
  body{background:var(--backdrop);font-family:"Montserrat",sans-serif;color:var(--text)}
  .spread{position:absolute;left:40px;top:20px;width:1120px;height:793px;display:flex;box-shadow:0 8px 24px rgba(0,0,0,.18)}
  .page{position:relative;width:560px;height:793px;background:var(--paper);overflow:hidden}
  .page--left{border-right:1px solid #dcdcdc}
  .heading{font-weight:700;color:var(--blue);font-size:27px;line-height:1.2;letter-spacing:.2px}
  .body-copy{font-size:8.5px;line-height:1.55;color:var(--text)}
  .sub-heading{font-weight:700;color:var(--blue);font-size:10px;margin-bottom:5px}

  /* left page */
  .intro{position:absolute;left:52px;top:46px;width:450px}
  .intro .body-copy{margin-top:12px}
  .steps{position:absolute;left:52px;top:150px;width:460px;display:flex;justify-content:space-between}
  .step{width:130px;text-align:center}
  .step-icon{width:76px;height:76px;border-radius:50%;margin:0 auto 14px;background:linear-gradient(150deg,var(--green-light),var(--green-dark));display:flex;align-items:center;justify-content:center}
  .quote-band{position:absolute;left:0;top:330px;width:560px;height:170px;display:flex}
  .quote{width:300px;background:linear-gradient(120deg,var(--green-dark),var(--green));padding:24px 30px 0 40px;color:var(--white)}
  .quote-mark{font-size:46px;line-height:.8;font-weight:700;font-style:italic}
  .quote p{font-size:10.5px;font-style:italic;font-weight:500;line-height:1.5;margin-top:4px}
  .photo{display:block}
  .photo--fittings{flex:1;background:linear-gradient(160deg,#3e3e40 0%,#6c6a68 55%,#b7a7a0 100%)}
  .stats{position:absolute;left:40px;top:530px;width:230px}
  .stat-row{display:flex;gap:26px}
  .stat{text-align:center}
  .stat .sub-heading{margin-bottom:6px}
  .stats .body-copy{margin-top:12px}
  .photo--green-parts{position:absolute;left:300px;top:575px;width:235px;height:170px;border-radius:40px;background:radial-gradient(ellipse at 50% 50%,#8fdc4a 0%,#5bbb2c 55%,#4aa526 100%)}

  /* right page */
  .photo--field{position:absolute;left:0;top:0;width:560px;height:300px;background:linear-gradient(90deg,#4e9a2a 0%,#6fbf3b 45%,#9aa19a 62%,#c9c6c0 100%)}
  .curve{position:absolute;left:0;top:150px}
  .about{position:absolute;left:40px;top:280px;width:210px}
  .about .body-copy,.services-intro .body-copy{margin-top:10px;text-align:justify}
  .photo--rolls{position:absolute;left:280px;top:300px;width:250px;height:290px;background:linear-gradient(135deg,#2c2c2c,#050505)}
  .services-intro{position:absolute;left:40px;top:435px;width:210px}
  .services{position:absolute;left:40px;top:615px;width:480px;display:grid;grid-template-columns:1fr 1fr;column-gap:30px;row-gap:30px}
  .service{display:flex;gap:12px;align-items:flex-start}
  .service-icon{flex:none;width:40px;height:40px;background:linear-gradient(150deg,var(--green-light),var(--green-dark));display:flex;align-items:center;justify-content:center}
  .service .body-copy{font-size:8px}
</style>
</head>
<body>
<div class="spread">

  <section class="page page--left">
    <div class="intro">
      <h2 class="heading">How It Works</h2>
      <p class="body-copy">Lorem ipsum dolor sit amet, consectetur adipiscing elit. Curabitur aliquet magna a nisl auctor, et egestas odio vestibulum. Suspendisse finibus porttitor nisl in iaculis. Sed tincidunt nulla sed tortor lacinia, at hendrerit dui lobortis.</p>
    </div>

    <div class="steps">
      <div class="step">
        <div class="step-icon">
          <svg width="34" height="34" viewBox="0 0 34 34" fill="none" stroke="#fff" stroke-width="1.6"><path d="M4 24l8-4 10 4 8-4v8l-8 4-10-4-8 4z"/><circle cx="17" cy="11" r="5"/><path d="M17 16v6"/></svg>
        </div>
        <h3 class="sub-heading">Lorem Ipsum Dolor</h3>
        <p class="body-copy">Lorem ipsum dolor sit amet, consectetur adipiscing elit. Curabitur aliquet magna a nisl auctor, et egestas vestibulum.</p>
      </div>
      <div class="step">
        <div class="step-icon">
          <svg width="34" height="34" viewBox="0 0 34 34" fill="none" stroke="#fff" stroke-width="1.6"><path d="M10 16l7-6 7 6v7H10z"/><path d="M4 26h8l6 3h8l4-4"/><path d="M15 23v-4h4v4"/></svg>
        </div>
        <h3 class="sub-heading">Lorem Ipsum Dolor</h3>
        <p class="body-copy">Lorem ipsum dolor sit amet, consectetur adipiscing elit. Curabitur aliquet magna a nisl auctor, et egestas vestibulum.</p>
      </div>
      <div class="step">
        <div class="step-icon">
          <svg width="34" height="34" viewBox="0 0 34 34" fill="none" stroke="#fff" stroke-width="1.6"><path d="M4 15L17 5l13 10"/><path d="M8 13v16h18V13"/><path d="M11 24l4-5 3 3 5-6"/></svg>
        </div>
        <h3 class="sub-heading">Lorem Ipsum Dolor</h3>
        <p class="body-copy">Lorem ipsum dolor sit amet, consectetur adipiscing elit. Curabitur aliquet magna a nisl auctor, et egestas vestibulum.</p>
      </div>
    </div>

    <div class="quote-band">
      <div class="quote">
        <div class="quote-mark">“</div>
        <p>Nam vestibulum at ante id lobortis. Suspendisse viverra diam at nisl aliquet aliquam. Aenean dignissim erat urna, vitae tincidunt eros commodo eget. Proin non pharetra erat. Sed efficitur suscipit.</p>
      </div>
      <div class="photo photo--fittings" role="img" aria-label="Row of metal pipeline fittings on a dark backdrop"></div>
    </div>

    <div class="stats">
      <div class="stat-row">
        <div class="stat">
          <h3 class="sub-heading">Lorem Ipsum</h3>
          <svg width="92" height="92" viewBox="0 0 92 92">
            <circle cx="46" cy="46" r="38" fill="none" stroke="var(--ring-track)" stroke-width="7"/>
            <circle cx="46" cy="46" r="38" fill="none" stroke="var(--green)" stroke-width="7" stroke-dasharray="155.2 238.8" transform="rotate(90 46 46)"/>
            <circle cx="46" cy="46" r="38" fill="none" stroke="var(--blue)" stroke-width="7" stroke-dasharray="83.6 238.8" stroke-dashoffset="-155.2" transform="rotate(90 46 46)"/>
            <text x="46" y="52" text-anchor="middle" font-family="Montserrat, sans-serif" font-size="17" font-style="italic" fill="#555">65%</text>
          </svg>
        </div>
        <div class="stat">
          <h3 class="sub-heading">Lorem Ipsum</h3>
          <svg width="92" height="92" viewBox="0 0 92 92">
            <circle cx="46" cy="46" r="38" fill="none" stroke="var(--ring-track)" stroke-width="7"/>
            <circle cx="46" cy="46" r="38" fill="none" stroke="var(--green)" stroke-width="7" stroke-dasharray="179.1 238.8" transform="rotate(90 46 46)"/>
            <circle cx="46" cy="46" r="38" fill="none" stroke="var(--blue)" stroke-width="7" stroke-dasharray="59.7 238.8" stroke-dashoffset="-179.1" transform="rotate(90 46 46)"/>
            <text x="46" y="52" text-anchor="middle" font-family="Montserrat, sans-serif" font-size="17" font-style="italic" fill="#555">75%</text>
          </svg>
        </div>
      </div>
      <p class="body-copy">Lorem ipsum dolor sit amet, consectetur adipiscing elit. Curabitur aliquet magna a nisl auctor, et egestas odio.</p>
    </div>

    <div class="photo photo--green-parts" role="img" aria-label="Green plastic pipeline centralizers and cable protectors"></div>
  </section>

  <section class="page page--right">
    <div class="photo photo--field" role="img" aria-label="Black pipeline pig tools resting on gravel beside green water"></div>
    <svg class="curve" width="560" height="160" viewBox="0 0 560 160" preserveAspectRatio="none">
      <path d="M0 160V70C180 -10 380 -10 560 70V160Z" fill="var(--paper)"/>
    </svg>

    <div class="about">
      <h2 class="heading">About Us</h2>
      <p class="body-copy">Lorem ipsum dolor sit amet, consectetur adipiscing elit. Curabitur aliquet magna a nisl auctor, et egestas odio vestibulum. Suspendisse finibus porttitor nisl in iaculis. Sed tincidunt nulla sed tortor lacinia, at hendrerit dui lobortis.</p>
    </div>

    <div class="photo photo--rolls" role="img" aria-label="Three product canisters of different sizes on a black background"></div>

    <div class="services-intro">
      <h2 class="heading">Our Services</h2>
      <p class="body-copy">Nam vestibulum at ante id lobortis. Suspendisse viverra diam at nisl aliquet aliquam. Aenean dignissim erat urna, vitae tincidunt eros commodo eget. Proin non pharetra erat. Sed efficitur suscipit tortor vehicula luctus.</p>
    </div>

    <div class="services">
      <div class="service">
        <div class="service-icon"><svg width="22" height="22" viewBox="0 0 22 22" fill="none" stroke="#fff" stroke-width="1.5"><rect x="3" y="9" width="16" height="10"/><rect x="2" y="6" width="18" height="3"/><path d="M11 6v13M11 6c-2-4-6-3-4-1M11 6c2-4 6-3 4-1"/></svg></div>
        <p class="body-copy">Lorem ipsum dolor sit amet, consectetur adipiscing elit. Curabitur aliquet magna a nisl auctor, et egestas odio vestibulum. Suspendisse finibus porttitor nisl.</p>
      </div>
      <div class="service">
        <div class="service-icon"><svg width="22" height="22" viewBox="0 0 22 22" fill="none" stroke="#fff" stroke-width="1.5"><path d="M3 10h4v9H3zM7 18h9l2-7h-6l1-5c0-2-2-2-3 0L7 11"/></svg></div>
        <p class="body-copy">Lorem ipsum dolor sit amet, consectetur adipiscing elit. Curabitur aliquet magna a nisl auctor, et egestas odio vestibulum. Suspendisse finibus porttitor nisl.</p>
      </div>
      <div class="service">
        <div class="service-icon"><svg width="22" height="22" viewBox="0 0 22 22" fill="none" stroke="#fff" stroke-width="1.5"><circle cx="11" cy="12" r="8"/><path d="M11 8v4l3 2M9 2h4"/></svg></div>
        <p class="body-copy">Lorem ipsum dolor sit amet, consectetur adipiscing elit. Curabitur aliquet magna a nisl auctor, et egestas odio vestibulum. Suspendisse finibus porttitor nisl.</p>
      </div>
      <div class="service">
        <div class="service-icon"><svg width="22" height="22" viewBox="0 0 22 22" fill="none" stroke="#fff" stroke-width="1.5"><circle cx="9" cy="9" r="6"/><path d="M13.5 13.5L20 20"/></svg></div>
        <p class="body-copy">Lorem ipsum dolor sit amet, consectetur adipiscing elit. Curabitur aliquet magna a nisl auctor, et egestas odio vestibulum. Suspendisse finibus porttitor nisl.</p>
      </div>
    </div>
  </section>

</div>
</body>
</html>
```